Modern Web Design for Nonprofit Organization

Our client is looking to redesign their website. They want a modern look, clean and professional, that integrates their new brand guidelines.

Here is clients current site:
http://www.valorandes.org/

They want their own unique design but here are some sites the clients likes:
https://www.brixtonvane.com/en/
https://oakhollowrise.org/
https://www.lumacraft.com/
https://www.tbnlawgroup.com/
https://www.greyharborco.org/

Attached please find the clients logos, color palette, site plan and design specs.

You will create a homepage mockup that will have the following sections in this order:
1. Thin Alert Bar at very top with one line message
2. Nav Bar with Logo and Main Nav (red in site plan)
3. Hero Image or Video
4. Signup Bar with name email and zip and connect button
5. Intro section with image, welcome message, and supporter counter
6. Featured Action section with call to action
7. Event section with two upcoming event cards
8. Latest News section with three latest blog post
9. Support our work (donation) section
10. Worker and Member Stories Section with feed of social posts
11. Footer.

You can use text and images from clients existing site or placeholder images and placeholder text.

Please submit as many home page mockups/idea boards as you like. Client will pick the top three and ask for some revisions. If you are selected this will lead to a lot of work for this client.

Project is private please adhere to ArtPlenary terms of use and do not share any materials please.

QUICKEST RESPONSE PLEASE!

Thanks for looking!

Target Market(s)

Non profit donors and farmworker advocates

Number of Pages Required

2 page

Font styles to use
Sans Serif

Requirements
Must have
• Adhere to brief and client brand ID
Nice to have
• World class design

```html
<!DOCTYPE html>
<html lang="en">
<head>
<meta charset="utf-8">
<title>Valor Andes Foundation — Home</title>
<link href="https://fonts.googleapis.com/css2?family=Montserrat:ital,wght@0,400;0,500;0,600;0,700;0,800;0,900;1,400&display=swap" rel="stylesheet">
<style>
:root{
  --red:#e3151b;
  --teal:#1f9aa0;
  --yellow:#fdc600;
  --ink:#111111;
  --grey-text:#8a8a8a;
  --light-bg:#f3f3f3;
  --card-bg:#f4f4f4;
  --white:#ffffff;
  --footer:#0d0d0d;
  --page-blue:#3a5a99;
  --chirp-blue:#2aa3ef;
  --snap-pink:#e23b6a;
}
*{box-sizing:border-box;margin:0;padding:0}
html,body{width:1200px;height:4413px;overflow:hidden}
body{font-family:"Montserrat",sans-serif;color:var(--ink);background:var(--white);position:relative}
section,header,footer{position:relative;width:1200px}
.pill{display:inline-flex;align-items:center;gap:14px;background:var(--red);color:#fff;font-weight:700;font-size:14px;border-radius:22px;height:42px;padding:0 30px 0 5px}
.pill .dot{width:32px;height:32px;border-radius:50%;background:#fff;display:flex;align-items:center;justify-content:center}
.section-title{font-weight:700;font-size:38px;text-align:center}
.glyph{display:inline-flex;align-items:center;justify-content:center;border-radius:50%;color:#fff;font-weight:700;font-family:"Montserrat",sans-serif}

/* alert */
.alert-bar{height:34px;background:var(--red);color:#fff;font-size:10px;font-weight:600;text-align:center;line-height:34px}
/* nav */
.nav-bar{height:57px;display:flex;align-items:center;padding:0 183px;background:#fff}
.brand{display:flex;align-items:center;gap:8px;font-weight:800;font-size:11.5px;line-height:1.05;width:177px}
.brand .mark{width:38px;height:38px;border-radius:50%;background:var(--red);flex:none}
.main-nav{display:flex;gap:15px;font-size:10.5px;font-weight:600;flex:1;padding-left:8px}
.nav-donate{border:2px solid var(--red);color:var(--red);border-radius:20px;height:38px;padding:0 12px 0 4px;display:flex;align-items:center;gap:10px;font-size:12px;font-weight:700}
.nav-donate .dot{width:26px;height:26px;border-radius:50%;background:var(--red);display:flex;align-items:center;justify-content:center}
/* hero */
.hero{height:526px;color:#fff;overflow:hidden;
  background:
   radial-gradient(ellipse 170px 120px at 790px 120px,rgba(214,34,30,.9),transparent 70%),
   radial-gradient(ellipse 150px 130px at 980px 160px,rgba(206,28,26,.95),transparent 70%),
   radial-gradient(ellipse 200px 150px at 860px 330px,rgba(190,24,22,.95),transparent 72%),
   radial-gradient(ellipse 150px 110px at 1080px 330px,rgba(200,30,26,.85),transparent 70%),
   radial-gradient(ellipse 330px 300px at 900px 270px,rgba(150,100,80,.55),transparent 75%),
   linear-gradient(90deg,#0e0e0e 0%,#1a1816 42%,#2e2420 58%,#3d2a24 80%,#221816 100%)}
.hero-text{position:absolute;left:183px;top:108px}
.hero h1{font-weight:900;font-size:68px;line-height:1.02}
.hero p{margin-top:16px;font-size:17.5px;line-height:1.5;width:370px}
.hero .pill{margin-top:26px}
/* signup */
.signup{height:391px;background:var(--teal);text-align:center;color:var(--ink)}
.signup h2{padding-top:44px;font-size:36px;font-weight:700}
.signup .underline{width:40px;height:3px;background:var(--ink);margin:4px auto 0}
.email-field{width:734px;height:56px;margin:20px auto 0;background:#fff;border-radius:28px;display:flex;align-items:center;gap:14px;padding:0 22px;font-size:13px;color:#555}
.signup-row{margin-top:24px;display:flex;justify-content:center;align-items:center;gap:18px;font-size:13px;font-weight:600}
.social-dot{width:22px;height:22px;border:2px solid var(--ink);color:var(--ink);font-size:10px;margin-left:5px;vertical-align:middle}
.sms-line{margin-top:22px;font-size:19px;font-weight:500}
.sms-line strong{font-weight:700}
.sms-line .hl{color:var(--red);font-weight:600}
.signup .note{margin:8px auto 0;width:700px;font-size:16px;line-height:1.6;color:#1c3c3e}
/* welcome */
.welcome{height:555px}
.welcome-frame{position:absolute;left:183px;top:99px;width:383px;height:381px;border:3px solid var(--red)}
.welcome-photo{position:absolute;left:206px;top:75px;width:382px;height:383px;
  background:
   radial-gradient(circle at 185px 40px,#fbf6e0 0,#e9dfb0 8%,rgba(120,100,60,.5) 22%,transparent 40%),
   linear-gradient(180deg,transparent 45%,rgba(255,240,200,.55) 52%,rgba(255,230,180,.5) 62%,transparent 70%),
   linear-gradient(180deg,#1b1812 0%,#2d2619 50%,#3b2b18 80%,#1e1710 100%)}
.welcome-text{position:absolute;left:660px;top:100px;width:355px}
.welcome-text h2{font-size:36px;font-weight:700;line-height:1.05}
.welcome-text p{font-size:12.5px;line-height:1.6;margin-top:16px;color:#222}
.welcome-text .pill{margin-top:20px}
/* events */
.events{height:655px;background:var(--light-bg)}
.events .section-title{padding-top:66px}
.event-card{position:absolute;left:233px;width:734px;height:135px;background:#fff;display:flex}
.event-thumb{width:142px;height:135px;flex:none}
.event-body{padding:26px 0 0 38px;width:420px}
.event-date{color:var(--red);font-size:11.5px;font-style:italic;display:flex;align-items:center;gap:6px}
.event-date i{width:12px;height:11px;background:var(--red);display:inline-block}
.event-title{font-weight:700;font-size:18.5px;margin-top:8px}
.event-desc{font-size:10px;color:#888;line-height:1.5;margin-top:8px;width:320px}
.event-actions{border-left:2px solid #ddd;height:54px;margin-top:40px;padding-left:36px;position:relative}
.event-actions .btns{position:absolute;left:36px;top:-12px;display:flex;flex-direction:column;gap:14px}
.event-actions a{width:124px;height:32px;border-radius:16px;display:flex;align-items:center;gap:14px;font-size:11px;font-weight:700;padding-left:4px}
.event-actions a span{width:24px;height:24px;border-radius:50%;background:#4a4a4a;display:flex;align-items:center;justify-content:center}
.btn-read{background:#d7dbdd}
.btn-visit{background:#fdf1b6}
.event-small{position:absolute;top:444px;width:358px;height:135px;background:#fff;padding:30px 0 0 28px}
.event-small .event-title{font-size:17px}
.event-small .event-desc{width:300px}
/* blog */
.blog{height:657px}
.blog .section-title{padding-top:64px}
.blog-grid{position:absolute;left:183px;top:148px;display:flex;gap:22px}
.blog-card{width:263px;height:355px;background:var(--card-bg)}
.blog-img{height:185px}
.blog-card h3{font-size:15.5px;font-weight:700;padding:28px 22px 0;white-space:nowrap}
.blog-card p{font-size:11.5px;color:#888;line-height:1.6;padding:10px 22px 0}
.blog-card .more{color:var(--red);font-weight:700;font-size:12px;padding:8px 22px 0;display:block}
.blog .center-btn{position:absolute;top:561px;left:0;width:1200px;text-align:center}
/* support */
.support{height:308px;background:var(--yellow);text-align:center}
.support h2{padding-top:64px;font-size:38px;font-weight:700}
.support p{width:640px;margin:18px auto 0;font-size:16px;line-height:1.5}
.support .pill{margin-top:24px}
/* stories */
.stories{height:828px}
.stories .section-title{padding-top:68px}
.story-cols{position:absolute;left:183px;top:144px;display:flex;gap:22px}
.story-col{width:263px;display:flex;flex-direction:column;gap:17px}
.story{background:#fff;box-shadow:0 2px 10px rgba(0,0,0,.12);position:relative}
.story-img{height:120px}
.story-body{padding:26px 26px 0;font-size:9.5px;color:#888;line-height:1.9}
.tag{display:inline-block;color:#fff;font-size:8px;font-weight:600;padding:3px 12px;margin-bottom:10px}
.tag.page{background:var(--page-blue)}.tag.chirp{background:var(--chirp-blue)}.tag.snap{background:var(--snap-pink)}
.story-body .link{color:#2a7ad0}
.story-body .at{color:#2a9a3a}
.corner{position:absolute;right:26px;width:16px;height:16px;font-size:8px}
.story-brand{display:flex;align-items:center;gap:6px;color:var(--ink);font-weight:800;font-size:8px;line-height:1;margin-top:8px}
.story-brand b{width:24px;height:24px;border-radius:50%;background:var(--ink)}
.story-foot{position:absolute;bottom:0;left:0;right:0;height:44px;border-top:1px solid #eee;display:flex;align-items:center;gap:18px;padding:0 20px;font-size:10px;color:#aaa}
.story-foot .share{margin-left:auto}
/* footer */
.site-footer{height:402px;background:var(--footer);color:#fff}
.footer-logo{position:absolute;left:214px;top:76px;width:80px;height:80px;border-radius:50%;background:#fff}
.footer-name{position:absolute;left:183px;top:162px;width:142px;text-align:center;font-weight:800;font-size:11px;line-height:1.15}
.lang{position:absolute;left:183px;top:200px;width:140px;height:34px;border:1px solid #fff;font-size:11px;display:flex;align-items:center;justify-content:center;gap:20px}
.f-col{position:absolute;top:78px}
.f-col h4{font-size:16px;font-weight:700;margin-bottom:18px}
.f-col li{list-style:none;font-size:11px;line-height:22.5px}
.contact-item{display:flex;gap:12px;font-size:9.5px;line-height:1.4;margin-bottom:18px}
.contact-item svg{flex:none}
.newsletter{width:245px;height:48px;border-radius:24px;background:#fff;display:flex;align-items:center;justify-content:space-between;padding:0 6px 0 26px;color:#777;font-size:12px}
.newsletter b{width:38px;height:38px;border-radius:50%;background:var(--red);display:flex;align-items:center;justify-content:center}
.f-socials{display:flex;gap:12px;margin-top:22px}
.f-socials span{width:32px;height:32px;background:var(--red);font-size:12px}
.copyright{position:absolute;left:0;right:0;top:292px;border-top:1px solid #333;padding-top:22px;text-align:center;font-size:11px}
</style>
</head>
<body>

<div class="alert-bar"><strong>ALERT:</strong> Lorem ipsum dolor sit amet, consectetur adipiscing elit, sed do eiusmod</div>

<header class="nav-bar">
  <div class="brand"><span class="mark"></span><span>VALOR ANDES<br>FOUNDATION</span></div>
  <nav class="main-nav"><span>Home</span><span>Get Help Now</span><span>Take Action</span><span>News And Eents</span><span>Support Our Work</span><span>About Us</span></nav>
  <div class="nav-donate"><span class="dot"><svg width="12" height="12" viewBox="0 0 14 14"><path d="M7 12 L2 7 A3 3 0 0 1 7 3 A3 3 0 0 1 12 7 Z" fill="#fff"/></svg></span>Donate Now</div>
</header>

<section class="hero" role="img" aria-label="Photo of many hands with red painted palms joined together in a circle">
  <div class="hero-text">
    <h1>Dona A<br>La Causa</h1>
    <p>Lorem ipsum dolor sit amet, consectetur adipiscing elit, sed do eiusmod tempor iidunt ut labore et dolore magna aliqua.</p>
    <div class="pill"><span class="dot"><svg width="14" height="14" viewBox="0 0 14 14"><path d="M7 12 L2 7 A3 3 0 0 1 7 3 A3 3 0 0 1 12 7 Z" fill="#e3151b"/></svg></span>Donate Now</div>
  </div>
</section>

<section class="signup">
  <h2>Stay Informed</h2>
  <div class="underline"></div>
  <div class="email-field"><svg width="18" height="13" viewBox="0 0 18 13"><rect x="1" y="1" width="16" height="11" fill="none" stroke="#777" stroke-width="1.5"/><path d="M1 1 L9 7 L17 1" fill="none" stroke="#777" stroke-width="1.5"/></svg>Enter Your Email Address</div>
  <div class="signup-row">
    <div class="pill"><span class="dot"><svg width="12" height="14" viewBox="0 0 12 14"><circle cx="6" cy="4" r="3" fill="#e3151b"/><path d="M0 14 A6 6 0 0 1 12 14Z" fill="#e3151b"/></svg></span>Sign up</div>
    <span style="font-weight:500">Or</span>
    <span>log In With: <span class="glyph social-dot">P</span><span class="glyph social-dot">S</span></span>
  </div>
  <p class="sms-line">Register With Your Phone Number <strong>Text "</strong><span class="hl">PAPELES</span><strong>" to</strong> <span class="hl">555-210</span></p>
  <p class="note">The VAF will never charge you for text messages but your phone company may charge you according to your plan.</p>
</section>

<section class="welcome">
  <div class="welcome-frame"></div>
  <div class="welcome-photo" role="img" aria-label="Night photo of a glowing light bulb above an illuminated marquee sign reading hope in a forest"></div>
  <div class="welcome-text">
    <h2>Welcome To<br>Valor Andes</h2>
    <p>Lorem ipsum dolor sit amet, consectetur adipiscing elit, sed do eiusmod tempor incididunt ut labore et dolore magna aliqua. Quis ipsum suspendisse ultrices gravida. Risus commodo viverra maecenas accumsan lacus vel facilisis.</p>
    <p>Lorem ipsum dolor sit amet, consectetur adipiscing elit, sed do eiusmod tempor incididunt ut labore et dolore magna aliqua.<br>&nbsp;Quis ipsum suspendisse ultrices gravida. Risus</p>
    <div class="pill"><span class="dot"><svg width="14" height="14" viewBox="0 0 14 14"><path d="M2 8 A5 5 0 0 1 12 8" fill="none" stroke="#e3151b" stroke-width="2"/><rect x="1" y="8" width="3" height="4" fill="#e3151b"/><rect x="10" y="8" width="3" height="4" fill="#e3151b"/></svg></span>Contact To our Support Counter</div>
  </div>
</section>

<section class="events">
  <h2 class="section-title">Featured Events</h2>
  <div class="event-card" style="top:143px">
    <div class="event-thumb" role="img" aria-label="Veterans day emblem with eagle and flag shield" style="background:radial-gradient(circle at 50% 55%,#d9d4c8 0,#8a8478 25%,#3a3a3a 55%,#222 100%)"></div>
    <div class="event-body">
      <div class="event-date"><i></i>Wed, 11 Nov 2020</div>
      <div class="event-title">Veterans Day in the United States</div>
      <div class="event-desc">In the USA, Veterans Day annually falls on November 11. This day is the anniversary of the signing of the...</div>
    </div>
    <div class="event-actions"><div class="btns">
      <a class="btn-read"><span><svg width="12" height="8" viewBox="0 0 14 10"><ellipse cx="7" cy="5" rx="6.5" ry="4.5" fill="#fff"/><circle cx="7" cy="5" r="2" fill="#4a4a4a"/></svg></span>Read More</a>
      <a class="btn-visit"><span><svg width="10" height="10" viewBox="0 0 10 10"><rect x="0.5" y="1.5" width="9" height="8" fill="none" stroke="#fff"/><rect x="0.5" y="1.5" width="9" height="2.5" fill="#fff"/></svg></span>Visit Event</a>
    </div></div>
  </div>
  <div class="event-card" style="top:294px">
    <div class="event-thumb" role="img" aria-label="Halloween illustration with moonlit castle and carved pumpkins" style="background:radial-gradient(circle at 45% 30%,#f2e6b8 0,#c9c3a0 12%,transparent 24%),radial-gradient(ellipse at 70% 95%,#f08a1c 0,#c7601a 25%,transparent 45%),linear-gradient(180deg,#1c2f5a,#0d1630 70%,#1a1206)"></div>
    <div class="event-body">
      <div class="event-date"><i></i>Sat, 31 Oct 2020</div>
      <div class="event-title">Halloween in the United States</div>
      <div class="event-desc">Many Americans celebrate Halloween on October 31. Celebr- ations include costume parties and trick-or-treating...</div>
    </div>
    <div class="event-actions"><div class="btns">
      <a class="btn-read"><span><svg width="12" height="8" viewBox="0 0 14 10"><ellipse cx="7" cy="5" rx="6.5" ry="4.5" fill="#fff"/><circle cx="7" cy="5" r="2" fill="#4a4a4a"/></svg></span>Read More</a>
      <a class="btn-visit"><span><svg width="10" height="10" viewBox="0 0 10 10"><rect x="0.5" y="1.5" width="9" height="8" fill="none" stroke="#fff"/><rect x="0.5" y="1.5" width="9" height="2.5" fill="#fff"/></svg></span>Visit Event</a>
    </div></div>
  </div>
  <div class="event-small" style="left:233px">
    <div class="event-date"><i></i>Wed, 11 Nov 2020</div>
    <div class="event-title">Veterans Day in the United States</div>
    <div class="event-desc">In the USA, Veterans Day annually falls on November 11. This day is the anniversary of the signing of the...</div>
  </div>
  <div class="event-small" style="left:608px">
    <div class="event-date"><i></i>Sat, 31 Oct 2020</div>
    <div class="event-title">Halloween in the United States</div>
    <div class="event-desc">Many Americans celebrate Halloween on October 31. Celebr- ations include costume parties and trick-or-treating...</div>
  </div>
</section>

<section class="blog">
  <h2 class="section-title">Latest Blog Post</h2>
  <div class="blog-grid">
    <article class="blog-card">
      <div class="blog-img" role="img" aria-label="Group photo of volunteers in matching shirts" style="background:radial-gradient(ellipse at 50% 35%,#a89a8a 0,#6e6356 40%,transparent 70%),linear-gradient(180deg,#7d8d9a 0%,#4a4a48 45%,#1f1d1b 75%,#b8961e 88%,#1f1d1b 100%)"></div>
      <h3>Open Hearth Kitchen...</h3>
      <p>Delano, California — More than 1,000 meals were distributed to families suffering from the coronavirus...</p>
      <span class="more">Read More &rarr;</span>
    </article>
    <article class="blog-card">
      <div class="blog-img" role="img" aria-label="Colourful children's drawing with hand-lettered message about giving" style="background:radial-gradient(ellipse at 30% 85%,#f2b8c8 0,transparent 35%),radial-gradient(ellipse at 70% 80%,#9fd0ec 0,transparent 35%),radial-gradient(ellipse at 50% 95%,#f4d36a 0,transparent 40%),linear-gradient(180deg,#f7f5ef 0%,#efe9dc 55%,#c8dfb0 100%)"></div>
      <h3>The Valor Andes...</h3>
      <p>Delano, California — More than 1,000 meals were distributed to families suffering from the coronavirus...</p>
      <span class="more">Read More &rarr;</span>
    </article>
    <article class="blog-card">
      <div class="blog-img" role="img" aria-label="Speaker addressing people at an outdoor cafe gathering" style="background:radial-gradient(ellipse at 80% 55%,#3b4a5a 0,transparent 30%),linear-gradient(180deg,#e6e8e2 0%,#b8b7a8 30%,#8a6e52 55%,#5a4a3a 80%,#3a322a 100%)"></div>
      <h3>Announcement: Corona...</h3>
      <p>Delano, California — More than 1,000 meals were distributed to families suffering from the coronavirus...</p>
      <span class="more">Read More &rarr;</span>
    </article>
  </div>
  <div class="center-btn"><div class="pill"><span class="dot"><svg width="14" height="10" viewBox="0 0 14 10"><ellipse cx="7" cy="5" rx="6.5" ry="4.5" fill="#e3151b"/><circle cx="7" cy="5" r="2" fill="#fff"/></svg></span>Vieww All Blog Posts</div></div>
</section>

<section class="support">
  <h2>Support Our Work</h2>
  <p>Lorem ipsum dolor sit amet, consectetur adipiscing elit, sed do eiusmod tempor incididunt ut labore et dolore magna aliqua.</p>
  <div class="pill"><span class="dot"><svg width="14" height="14" viewBox="0 0 14 14"><path d="M7 12 L2 7 A3 3 0 0 1 7 3 A3 3 0 0 1 12 7 Z" fill="#e3151b"/></svg></span>Donate Now</div>
</section>

<section class="stories">
  <h2 class="section-title">Succes Stories</h2>
  <div class="story-cols">
    <div class="story-col">
      <div class="story" style="height:226px">
        <span class="glyph corner" style="top:28px;background:var(--page-blue)">P</span>
        <div class="story-body"><span class="tag page">PAGEBOOK</span><br>Chirper &amp; <span class="at">@SpeedLeague</span> are taking you to the Ridgeway 400 with <span class="link">http://vaf.link/8kTqRw</span>.<br>Read more: <span class="link">http://vaf.link/3mPzXa</span>
          <div class="story-brand"><b></b>VALOR ANDES<br>FOUNDATION</div></div>
        <div class="story-foot"><span>&#8617;</span><span>&#8645; 6</span><span>&#9825; 17</span><span class="share">&#8679;</span></div>
      </div>
      <div class="story" style="height:366px">
        <div class="story-img" role="img" aria-label="Close-up of a desk globe" style="background:radial-gradient(circle at 62% 55%,#6fb0c8 0,#3f7f99 22%,#c79a4a 36%,transparent 48%),linear-gradient(135deg,#2a1e14,#6a4e2c 50%,#2a2018)"></div>
        <span class="glyph corner" style="top:148px;background:var(--chirp-blue)">C</span>
        <div class="story-body"><span class="tag chirp">CHIRPER</span><br>Chirper &amp; <span class="at">@SpeedLeague</span> are taking you to the Ridgeway 400 with <span class="link">http://vaf.link/8kTqRw</span>.<br>Read more: <span class="link">http://vaf.link/3mPzXa</span>
          <div class="story-brand"><b></b>VALOR ANDES<br>FOUNDATION</div></div>
        <div class="story-foot"><span>&#8617;</span><span>&#8645; 6</span><span>&#9825; 17</span><span class="share">&#8679;</span></div>
      </div>
    </div>
    <div class="story-col">
      <div class="story" style="height:440px">
        <div class="story-img" role="img" aria-label="Two cups of latte art held together over a table" style="height:200px;background:radial-gradient(circle at 38% 62%,#e8cfa8 0,#b88a5a 12%,#2a1e16 22%,transparent 30%),radial-gradient(circle at 64% 42%,#e8cfa8 0,#b88a5a 12%,#2a1e16 22%,transparent 30%),linear-gradient(135deg,#8a6a4e,#4a3424 50%,#2a1e16)"></div>
        <span class="glyph corner" style="top:230px;background:var(--chirp-blue)">C</span>
        <div class="story-body"><span class="tag chirp">CHIRPER</span><br>Chirper &amp; <span class="at">@SpeedLeague</span> are taking you to the Ridgeway 400 with <span class="link">http://vaf.link/8kTqRw</span>.<br>Read more: <span class="link">http://vaf.link/3mPzXa</span>
          <div class="story-brand"><b></b>VALOR ANDES<br>FOUNDATION</div></div>
        <div class="story-foot"><span>&#8617;</span><span>&#8645; 6</span><span>&#9825; 17</span><span class="share">&#8679;</span></div>
      </div>
      <div class="story" style="height:152px">
        <span class="glyph corner" style="top:26px;background:var(--page-blue)">P</span>
        <div class="story-body"><span class="tag page">PAGEBOOK</span><br>Chirper &amp; <span class="at">@SpeedLeague</span> are taking you to the Ridgeway 400 with <span class="link">http://vaf.link/8kTqRw</span>.</div>
        <div class="story-foot"><span>&#8617;</span><span>&#8645; 6</span><span>&#9825; 17</span><span class="share">&#8679;</span></div>
      </div>
    </div>
    <div class="story-col">
      <div class="story" style="height:341px">
        <div class="story-img" role="img" aria-label="Group of young friends talking outdoors" style="background:radial-gradient(ellipse at 60% 70%,#f1f1ee 0,transparent 25%),radial-gradient(ellipse at 85% 75%,#e6b93a 0,transparent 22%),linear-gradient(135deg,#b9c8d2,#d9cfb6 45%,#7f9a5a 80%,#5c7440)"></div>
        <span class="glyph corner" style="top:148px;background:var(--snap-pink)">S</span>
        <div class="story-body"><span class="tag snap">SNAPGRAM</span><br>Chirper &amp; <span class="at">@SpeedLeague</span> are taking you to the Ridgeway 400 with <span class="link">http://vaf.link/8kTqRw</span>.<br>Read more: <span class="link">http://vaf.link/3mPzXa</span>
          <div class="story-brand"><b></b>VALOR ANDES<br>FOUNDATION</div></div>
        <div class="story-foot"><span>&#8617;</span><span>&#8645; 6</span><span>&#9825; 17</span><span class="share">&#8679;</span></div>
      </div>
      <div class="story" style="height:251px">
        <span class="glyph corner" style="top:28px;background:var(--snap-pink)">S</span>
        <div class="story-body"><span class="tag snap">SNAPGRAM</span><br>Chirper &amp; <span class="at">@SpeedLeague</span> are taking you to the Ridgeway 400 with <span class="link">http://vaf.link/8kTqRw</span>.<br>Read more: <span class="link">http://vaf.link/3mPzXa</span>
          <div class="story-brand"><b></b>VALOR ANDES<br>FOUNDATION</div></div>
        <div class="story-foot"><span>&#8617;</span><span>&#8645; 6</span><span>&#9825; 17</span><span class="share">&#8679;</span></div>
      </div>
    </div>
  </div>
</section>

<footer class="site-footer">
  <div class="footer-logo"></div>
  <div class="footer-name">VALOR ANDES<br>FOUNDATION</div>
  <div class="lang"><span>English</span><span>&#9662;</span></div>
  <div class="f-col" style="left:391px">
    <h4>Quick Links</h4>
    <ul><li>Home</li><li>Get Help Now</li><li>Take Action</li><li>News And Events</li><li>Support Our Work</li><li>About Us</li></ul>
  </div>
  <div class="f-col" style="left:559px">
    <h4>Contact Us</h4>
    <div class="contact-item"><svg width="10" height="14" viewBox="0 0 10 14"><path d="M5 14 C1 8 0 6 0 5 A5 5 0 0 1 10 5 C10 6 9 8 5 14Z" fill="#fff"/><circle cx="5" cy="5" r="2" fill="#0d0d0d"/></svg><span>Somewhere, any street,<br>123456789, USA</span></div>
    <div class="contact-item"><svg width="10" height="14" viewBox="0 0 10 14"><rect x="1" y="0.5" width="8" height="13" rx="1.5" fill="none" stroke="#fff" stroke-width="1.5"/></svg><span><b>Call Us</b><br>+1 (555) 014-7790</span></div>
    <div class="contact-item"><svg width="12" height="12" viewBox="0 0 12 12"><rect x="0" y="4" width="12" height="8" fill="#fff"/><rect x="3" y="0" width="6" height="5" fill="#fff"/></svg><span><b>Fax</b><br>+1 (555) 014-7790</span></div>
  </div>
  <div class="f-col" style="left:771px">
    <h4>Suubscribe Newsletter</h4>
    <div class="newsletter">Email address<b><svg width="16" height="14" viewBox="0 0 16 14"><path d="M0 6 L16 0 L11 14 L8 8 Z" fill="#fff"/></svg></b></div>
    <div class="f-socials"><span class="glyph">P</span><span class="glyph">C</span><span class="glyph">S</span></div>
  </div>
  <div class="copyright">Copyright &copy; Valor Andes Foundation 2020. All right Reserved</div>
</footer>

</body>
</html>
```